Search Fund needs a PowerPoint template design

We need a eye-catching and compelling PowerPoint design for a new company based in Chicago called Tarn Ridge Partners. We are search fund with a primary mission to acquire a founder/family/entrepreneur owned businesses (This is similar to a Private Equity firm). Our goal is to offer investors a unique avenue to invest in an attractive business acquisition while providing business owners with an alternative path to exit. We would like the design to reflect crisp and professional nature that many financial firms present. The template should build on the design of the logo including expanding a logical color palette. The presentation will be used to describe facts regarding the firm, financial data and key messaging that we want our investors and potential partners to takeaway.

Target Market(s)

Financial Investors

Industry/Entity Type

Finance

Font styles to use
Serif
Sans Serif

Colors

Designer to choose colors to be used in the design.

Requirements
Must have
• Should include cover page and slide examples. Attractive data displays (graphs, charts, infographics etc.); Compelling cover; fly pages to put in between sections; table of contents page. Needs to have white space to add text.
Should not have
• Do not redesign the logo or change the logo colors. Additional colors should be added to the PowerPoint template

```html
<!DOCTYPE html>
<html lang="en">
<head>
<meta charset="utf-8">
<title>Tarn Ridge Partners — Presentation Template</title>
<link href="https://fonts.googleapis.com/css2?family=Lato:wght@300;400;700;900&display=swap" rel="stylesheet">
<style>
:root{
  --blue:#1a6fb5;
  --blue-dark:#0f4f8a;
  --navy:#0d2a4a;
  --sky:#dbe9f5;
  --grey:#9b9b9b;
  --grey-mid:#b5b5b5;
  --grey-light:#e7e7e7;
  --orange:#e8702a;
  --green:#7ab648;
  --ink:#444;
  --white:#fff;
}
*{box-sizing:border-box;margin:0;padding:0}
html,body{width:1200px;height:2287px;overflow:hidden;background:#fff}
body{font-family:'Lato',sans-serif;color:var(--ink)}
.sheet{display:grid;grid-template-columns:repeat(3,394px);grid-auto-rows:221px;gap:7.5px 8px;padding:3px 1px}
.slide{position:relative;overflow:hidden;background:var(--white)}
.abs{position:absolute}
.ttl{position:absolute;left:10px;top:14px;font-size:11px;color:var(--blue);font-weight:400}
.ttl::before{content:"";position:absolute;left:0;top:-7px;width:22px;height:3px;background:var(--grey-mid)}
.foot{position:absolute;left:0;right:0;bottom:0;height:10px;background:var(--grey-light);font-size:4.5px;color:#888;display:flex;align-items:center;justify-content:space-between;padding:0 8px}
.foot b{color:var(--navy);font-size:5.5px;font-weight:900;letter-spacing:.5px}
.tiny{font-size:4px;line-height:1.45;color:#777}
.small{font-size:5px;line-height:1.4;color:#666}
.wt{color:var(--white)}
.photo{position:absolute}
.ph-blue{background:linear-gradient(135deg,#0c4a86,#2c86cf 55%,#6fb0e0)}
.ph-road{background:linear-gradient(160deg,#24344a,#58708d 60%,#a9b7c6)}
.ph-sky{background:linear-gradient(160deg,#9fc7ea,#3e7fbc)}
.ph-grey{background:linear-gradient(160deg,#cfd4d9,#8f98a2)}
.ph-dark{background:linear-gradient(160deg,#2a3340,#6b7686)}
.ph-soft{background:linear-gradient(180deg,#eef1f4,#cdd4db)}
.brand{font-weight:900;color:var(--white);letter-spacing:1px;line-height:1}
.dot{display:inline-block;width:6px;height:6px;border-radius:50%;vertical-align:middle}
.ico{display:inline-flex;align-items:center;justify-content:center;width:12px;height:12px;border-radius:50%;color:#fff;font-size:6px;font-weight:700}
.bg-blue{background:var(--blue)}.bg-grey{background:var(--grey)}.bg-orange{background:var(--orange)}.bg-green{background:var(--green)}.bg-navy{background:var(--navy)}
.c-blue{color:var(--blue)}.c-orange{color:var(--orange)}.c-grey{color:var(--grey)}.c-green{color:var(--green)}
.h6{font-size:6px;font-weight:700}
table.data{border-collapse:collapse;font-size:4px;width:100%}
table.data th{background:var(--blue);color:#fff;font-weight:700;padding:2px}
table.data td{padding:1.8px 2px;text-align:center;color:#555}
table.data tr:nth-child(even) td{background:var(--sky)}
table.data td:first-child{background:var(--blue);color:#fff;text-align:left}
</style>
</head>
<body>
<main class="sheet">

<section class="slide">
  <div class="photo ph-blue" style="inset:0" role="img" aria-label="Blue-toned photo of glass office towers"></div>
  <div class="abs brand" style="left:22px;top:96px;font-size:12px">TARN RIDGE<br>PARTNERS</div>
  <div class="abs" style="left:126px;top:90px;width:1px;height:34px;background:#fff"></div>
  <div class="abs wt" style="left:140px;top:90px;font-size:19px;font-weight:300;line-height:1.1">YOUR PRESENTATION<br>TITLE GOESHERE</div>
  <div class="abs wt" style="right:14px;bottom:10px;font-size:5px">www.tarnridgepartners.com</div>
</section>

<section class="slide">
  <div class="photo ph-blue" style="inset:0" role="img" aria-label="Looking up at a blue glass skyscraper"></div>
  <div class="abs" style="left:80px;top:94px;width:70px;height:24px;background:rgba(255,255,255,.25)"></div>
  <div class="abs brand" style="left:86px;top:98px;font-size:8px">TARN RIDGE<br>PARTNERS</div>
  <div class="abs wt" style="left:84px;top:150px;font-size:19px;font-weight:300">YOUR TITLE GOES HERE</div>
  <div class="abs wt" style="left:84px;top:175px;font-size:7px">Subtitle Here</div>
  <div class="abs wt" style="right:14px;top:8px;font-size:5px">www.tarnridgepartners.com</div>
</section>

<section class="slide">
  <div class="ttl">ABOUT US</div>
  <div class="abs tiny" style="left:10px;top:32px;right:12px">
    <p>Our firm partners with founders and families who are ready for a new chapter. We seek one strong, steady company and commit to leading it for the long run. Investors back a single focused search, owners gain a trusted buyer who protects their people, their name and the work they built over many years. We study each market with care before we act.</p><br>
    <p>We look for durable firms with loyal clients, steady cash flow and room to grow. Our process is simple and open: a first call, a site visit, a clear offer and a fair close. After the deal we stay close to the team, keep what works and invest where it counts. We report to our partners each quarter with plain numbers.</p><br>
    <p>Our team brings years of work in lending, operations and advisory roles. We believe patient capital, honest talks and clear goals make the best results for all sides. This page can hold your story, your mission and the reasons partners choose to work with you today.</p>
  </div>
  <div class="foot"><span>© Copyright 2024 Tarn Ridge Partners</span><span>3</span></div>
</section>

<section class="slide">
  <div class="ttl">Market Overview</div>
  <div class="abs bg-navy" style="left:10px;top:32px;width:88px;height:110px"></div>
  <div class="abs" style="left:16px;top:40px;width:10px;height:10px;border:1px solid #fff"></div>
  <div class="abs wt h6" style="left:30px;top:40px">Heading Text</div>
  <div class="abs tiny" style="left:30px;top:48px;width:62px;color:#cfe">Short note on market size and trend lines.</div>
  <div class="abs" style="left:16px;top:88px;width:10px;height:10px;border:1px solid #fff"></div>
  <div class="abs wt h6" style="left:30px;top:88px">Heading Text</div>
  <div class="abs tiny" style="left:30px;top:96px;width:62px;color:#cfe">Short note on buyer demand by region.</div>
  <div class="photo ph-dark" style="left:98px;top:32px;width:90px;height:65px" role="img" aria-label="Photo of a modern workspace"></div>
  <svg class="abs" style="left:198px;top:34px" width="58" height="58" viewBox="0 0 58 58"><circle cx="29" cy="29" r="23" fill="none" stroke="#dde6ef" stroke-width="6"/><circle cx="29" cy="29" r="23" fill="none" stroke="#4aa3e0" stroke-width="6" stroke-dasharray="86.7 144.5" transform="rotate(-90 29 29)"/><text x="29" y="33" text-anchor="middle" font-size="11" fill="#777" font-family="Lato">60%</text></svg>
  <div class="abs bg-blue" style="left:300px;top:28px;width:94px;height:100px"></div>
  <div class="abs wt h6" style="left:308px;top:36px">Heading Text</div>
  <div class="abs tiny wt" style="left:308px;top:44px;width:80px;color:#fff">Brief line about share of deals closed.</div>
  <div class="abs wt h6" style="left:308px;top:64px">Heading Text</div>
  <div class="abs tiny wt" style="left:308px;top:72px;width:80px;color:#fff">Brief line about growth in the sector.</div>
  <div class="abs wt h6" style="left:308px;top:92px">Heading Text</div>
  <div class="abs tiny wt" style="left:308px;top:100px;width:80px;color:#fff">Brief line about future outlook.</div>
  <div class="abs h6 c-blue" style="left:106px;top:108px">Heading Text</div>
  <div class="abs tiny" style="left:106px;top:116px;width:190px">Use this space to outline the market you target, the size of each segment and the reasons it fits the fund. Keep it short and clear so partners can scan the key points quickly.</div>
  <div class="foot"><b>TARN RIDGE</b><span>© Copyright 2024 Tarn Ridge Partners</span><span>4</span></div>
</section>

<section class="slide">
  <div class="ttl">Bullets Point 1 Level</div>
  <div class="abs" style="left:20px;top:55px;width:110px"><span class="dot bg-blue"></span> <span class="h6 c-blue">Your Text Here</span><div class="tiny" style="margin-left:9px">Lorem ipsum dolor sit amet, consectetur adipiscing elit sed do.</div></div>
  <div class="abs" style="left:142px;top:55px;width:110px"><span class="dot bg-grey"></span> <span class="h6 c-grey">Your Text Here</span><div class="tiny" style="margin-left:9px">Lorem ipsum dolor sit amet, consectetur adipiscing elit sed do.</div></div>
  <div class="abs" style="left:264px;top:55px;width:110px"><span class="dot bg-orange"></span> <span class="h6 c-orange">Your Text Here</span><div class="tiny" style="margin-left:9px">Lorem ipsum dolor sit amet, consectetur adipiscing elit sed do.</div></div>
  <div class="abs" style="left:20px;top:130px;width:110px"><span class="dot bg-blue"></span> <span class="h6 c-blue">Your Text Here</span><div class="tiny" style="margin-left:9px">Lorem ipsum dolor sit amet, consectetur adipiscing elit sed do.</div></div>
  <div class="abs" style="left:142px;top:130px;width:110px"><span class="dot bg-grey"></span> <span class="h6 c-grey">Your Text Here</span><div class="tiny" style="margin-left:9px">Lorem ipsum dolor sit amet, consectetur adipiscing elit sed do.</div></div>
  <div class="abs" style="left:264px;top:130px;width:110px"><span class="dot bg-orange"></span> <span class="h6 c-orange">Your Text Here</span><div class="tiny" style="margin-left:9px">Lorem ipsum dolor sit amet, consectetur adipiscing elit sed do.</div></div>
  <div class="foot"><b>TARN RIDGE</b><span>© Copyright 2024 Tarn Ridge Partners</span><span>5</span></div>
</section>

<section class="slide">
  <div class="abs bg-blue" style="left:180px;top:20px;width:200px;height:170px"></div>
  <div class="photo ph-dark" style="left:30px;top:55px;width:145px;height:100px" role="img" aria-label="Desktop monitor showing a city skyline at night"></div>
  <div class="abs wt" style="left:226px;top:50px;font-size:11px;line-height:1.3">Awesome<br>Mockup<br>Picture</div>
  <div class="abs tiny" style="left:226px;top:108px;width:110px;color:#fff">Place a screen shot of your report, portal or deal room in the frame to show work in progress.</div>
  <div class="foot"><b>TARN RIDGE</b><span>© Copyright 2024 Tarn Ridge Partners</span><span>6</span></div>
</section>

<section class="slide">
  <div class="ttl">Our Differences</div>
  <div class="abs bg-blue" style="left:20px;top:58px;width:355px;height:80px"></div>
  <div class="abs" style="left:30px;top:64px;width:210px">
    <div class="tiny" style="color:#fff;margin-bottom:6px"><span class="ico" style="background:#fff;color:var(--blue);width:9px;height:9px">✓</span> Patient capital with a long hold view.</div>
    <div class="tiny" style="color:#fff;margin-bottom:6px"><span class="ico" style="background:#fff;color:var(--blue);width:9px;height:9px">✓</span> Owner legacy and staff kept at the core.</div>
    <div class="tiny" style="color:#fff;margin-bottom:6px"><span class="ico" style="background:#fff;color:var(--blue);width:9px;height:9px">✓</span> Clear, fair terms and a fast close.</div>
    <div class="tiny" style="color:#fff"><span class="ico" style="background:#fff;color:var(--blue);width:9px;height:9px">✓</span> Hands-on leadership after the deal.</div>
  </div>
  <div class="photo ph-grey" style="left:255px;top:66px;width:110px;height:64px" role="img" aria-label="Photo of a silver car"></div>
  <div class="foot"><b>TARN RIDGE</b><span>© Copyright 2024 Tarn Ridge Partners</span><span>7</span></div>
</section>

<section class="slide" style="display:flex">
  <div style="flex:1;background:#8a8a8a"></div><div style="flex:1;background:#9a9a9a"></div><div style="flex:1;background:#a8a8a8"></div><div style="flex:1;background:#b6b6b6"></div><div style="flex:1;background:var(--blue)"></div>
  <div class="abs" style="inset:0;display:flex">
    <div style="flex:1;padding:40px 6px 0;text-align:center" class="wt"><div style="font-size:14px">⚙</div><div style="font-size:7px;margin-top:44px">Heading Here</div><div class="tiny" style="color:#fff;margin-top:4px">Lorem ipsum dolor sit amet consectetur elit sed do eiusmod tempor.</div></div>
    <div style="flex:1;padding:40px 6px 0;text-align:center" class="wt"><div style="font-size:14px">▤</div><div style="font-size:7px;margin-top:44px">Heading Here</div><div class="tiny" style="color:#fff;margin-top:4px">Lorem ipsum dolor sit amet consectetur elit sed do eiusmod tempor.</div></div>
    <div style="flex:1;padding:40px 6px 0;text-align:center" class="wt"><div style="font-size:14px">⌕</div><div style="font-size:7px;margin-top:44px">Heading Here</div><div class="tiny" style="color:#fff;margin-top:4px">Lorem ipsum dolor sit amet consectetur elit sed do eiusmod tempor.</div></div>
    <div style="flex:1;padding:40px 6px 0;text-align:center" class="wt"><div style="font-size:14px">☐</div><div style="font-size:7px;margin-top:44px">Heading Here</div><div class="tiny" style="color:#fff;margin-top:4px">Lorem ipsum dolor sit amet consectetur elit sed do eiusmod tempor.</div></div>
    <div style="flex:1;padding:40px 6px 0;text-align:center" class="wt"><div style="font-size:14px">◎</div><div style="font-size:7px;margin-top:44px">Heading Here</div><div class="tiny" style="color:#fff;margin-top:4px">Lorem ipsum dolor sit amet consectetur elit sed do eiusmod tempor.</div></div>
  </div>
  <div class="foot" style="background:#7a7a7a"></div>
</section>

<section class="slide">
  <div class="abs bg-blue" style="left:0;top:0;width:185px;height:211px"></div>
  <div class="abs wt" style="left:54px;top:36px;width:68px;height:68px;border:2px solid #fff;border-radius:50%;display:flex;align-items:center;justify-content:center;text-align:center;font-size:8px;line-height:1.2">RIGHT<br>PICTURE<br>SLIDE</div>
  <div class="abs tiny" style="left:40px;top:122px;width:115px;color:#fff">Lorem ipsum dolor sit amet consectetur adipiscing elit sed do eiusmod tempor incididunt ut labore.</div>
  <svg class="abs" style="left:200px;top:30px" width="180" height="100" viewBox="0 0 180 100">
    <line x1="0" y1="96" x2="180" y2="96" stroke="#ccc" stroke-width=".6"/>
    <rect x="10" y="40" width="7" height="56" fill="#1a6fb5"/><rect x="19" y="30" width="7" height="66" fill="#9b9b9b"/><rect x="28" y="55" width="7" height="41" fill="#e8702a"/>
    <rect x="55" y="50" width="7" height="46" fill="#1a6fb5"/><rect x="64" y="20" width="7" height="76" fill="#9b9b9b"/><rect x="73" y="60" width="7" height="36" fill="#e8702a"/>
    <rect x="100" y="10" width="7" height="86" fill="#1a6fb5"/><rect x="109" y="45" width="7" height="51" fill="#9b9b9b"/><rect x="118" y="35" width="7" height="61" fill="#e8702a"/>
    <rect x="145" y="30" width="7" height="66" fill="#1a6fb5"/><rect x="154" y="55" width="7" height="41" fill="#9b9b9b"/><rect x="163" y="15" width="7" height="81" fill="#e8702a"/>
  </svg>
  <div class="abs" style="left:210px;top:138px;font-size:18px;font-weight:700;color:var(--orange)"><span style="color:var(--blue);font-size:10px">▲</span> 85%</div>
  <div class="abs tiny" style="left:225px;top:162px;width:80px">Profit growth over the last year across all holdings.</div>
  <div class="foot"><b>TARN RIDGE</b><span>© Copyright 2024 Tarn Ridge Partners</span><span>9</span></div>
</section>

<section class="slide">
  <div class="ttl">Your Title Goes Here</div>
  <div class="photo ph-sky" style="left:20px;top:40px;width:95px;height:62px" role="img" aria-label="Photo of a bridge against the sky"></div>
  <div class="abs bg-grey" style="left:118px;top:40px;width:135px;height:62px"></div>
  <div class="abs wt h6" style="left:150px;top:55px">Heading Goes Here</div>
  <div class="abs tiny" style="left:128px;top:66px;width:115px;color:#fff">Lorem ipsum dolor sit amet, consectetur adipiscing elit sed do.</div>
  <div class="photo ph-blue" style="left:256px;top:40px;width:114px;height:62px" role="img" aria-label="Photo of a glass tower"></div>
  <div class="abs bg-blue" style="left:20px;top:105px;width:120px;height:62px"></div>
  <div class="abs wt h6" style="left:32px;top:120px">Heading Goes Here</div>
  <div class="abs tiny" style="left:28px;top:131px;width:105px;color:#fff">Lorem ipsum dolor sit amet, consectetur adipiscing elit.</div>
  <div class="photo ph-sky" style="left:143px;top:105px;width:110px;height:62px" role="img" aria-label="Photo of a modern glass ceiling"></div>
  <div class="abs bg-orange" style="left:256px;top:105px;width:114px;height:62px"></div>
  <div class="abs wt h6" style="left:266px;top:120px">Heading Goes Here</div>
  <div class="abs tiny" style="left:264px;top:131px;width:100px;color:#fff">Lorem ipsum dolor sit amet, consectetur adipiscing elit.</div>
  <div class="foot"><b>TARN RIDGE</b><span>© Copyright 2024 Tarn Ridge Partners</span><span>10</span></div>
</section>

<section class="slide">
  <div class="photo ph-sky" style="inset:0" role="img" aria-label="Business people walking past a glass wall with a city view"></div>
  <div class="abs" style="left:200px;top:50px;width:194px;height:100px;background:rgba(26,111,181,.88)"></div>
  <div class="abs wt" style="left:214px;top:68px;font-size:10px">ABOUT US</div>
  <div class="abs tiny" style="left:214px;top:88px;width:160px;color:#fff">Lorem ipsum dolor sit amet, consectetur adipiscing elit sed do eiusmod tempor incididunt ut labore. Ut enim ad minim veniam quis nostrud.</div>
</section>

<section class="slide" style="background:var(--blue)">
  <div class="abs bg-grey" style="left:0;top:0;right:0;height:70px"></div>
  <div class="abs" style="left:0;top:82px;width:185px;height:30px;background:#0f5f9f"></div>
  <div class="abs brand" style="left:70px;top:88px;font-size:9px">TARN RIDGE<br>PARTNERS</div>
  <div class="abs wt" style="left:52px;top:140px;font-size:16px;font-weight:300">This Is Your Divider Page</div>
  <div class="abs wt" style="left:52px;top:162px;font-size:5.5px">Your Subtitle Goes Here</div>
</section>

<section class="slide">
  <div class="ttl">Brand Detailed</div>
  <div class="photo ph-road" style="left:20px;top:40px;width:180px;height:135px" role="img" aria-label="Photo of a busy highway at dusk"></div>
  <div class="abs bg-blue" style="left:202px;top:40px;width:80px;height:66px"></div>
  <div class="abs bg-grey" style="left:284px;top:40px;width:86px;height:66px"></div>
  <div class="abs bg-orange" style="left:202px;top:108px;width:80px;height:67px"></div>
  <div class="abs bg-green" style="left:284px;top:108px;width:86px;height:67px"></div>
  <div class="abs wt h6" style="left:202px;top:50px;width:80px;text-align:center">System</div><div class="abs tiny" style="left:210px;top:60px;width:66px;color:#fff;text-align:center">Lorem ipsum dolor sit amet elit sed do eiusmod.</div>
  <div class="abs wt h6" style="left:284px;top:50px;width:86px;text-align:center">Technology</div><div class="abs tiny" style="left:292px;top:60px;width:72px;color:#fff;text-align:center">Lorem ipsum dolor sit amet elit sed do eiusmod.</div>
  <div class="abs wt h6" style="left:202px;top:118px;width:80px;text-align:center">Leisure</div><div class="abs tiny" style="left:210px;top:128px;width:66px;color:#fff;text-align:center">Lorem ipsum dolor sit amet elit sed do eiusmod.</div>
  <div class="abs wt h6" style="left:284px;top:118px;width:86px;text-align:center">Digital</div><div class="abs tiny" style="left:292px;top:128px;width:72px;color:#fff;text-align:center">Lorem ipsum dolor sit amet elit sed do eiusmod.</div>
  <div class="foot"><b>TARN RIDGE</b><span>© Copyright 2024 Tarn Ridge Partners</span><span>13</span></div>
</section>

<section class="slide">
  <div class="ttl">Product Philosophy</div>
  <svg class="abs" style="left:145px;top:55px" width="105" height="105" viewBox="0 0 42 42">
    <circle cx="21" cy="21" r="15.9" fill="none" stroke="#9b9b9b" stroke-width="7" stroke-dasharray="21 79" stroke-dashoffset="25"/>
    <circle cx="21" cy="21" r="15.9" fill="none" stroke="#e8702a" stroke-width="7" stroke-dasharray="22 78" stroke-dashoffset="4"/>
    <circle cx="21" cy="21" r="15.9" fill="none" stroke="#7ab648" stroke-width="7" stroke-dasharray="20 80" stroke-dashoffset="-18"/>
    <circle cx="21" cy="21" r="15.9" fill="none" stroke="#1a6fb5" stroke-width="7" stroke-dasharray="37 63" stroke-dashoffset="-38"/>
    <rect x="17" y="17" width="8" height="8" fill="#1a6fb5"/>
  </svg>
  <div class="abs wt" style="left:156px;top:104px;font-size:5px">40%</div>
  <div class="abs wt" style="left:206px;top:66px;font-size:5px">15%</div>
  <div class="abs wt" style="left:232px;top:104px;font-size:5px">20%</div>
  <div class="abs wt" style="left:192px;top:146px;font-size:5px">20%</div>
  <div class="abs" style="left:20px;top:45px;width:95px;text-align:right"><div class="h6 c-blue">Insure</div><div class="tiny">Nullam eu tempor elit, et mattis lectus vel risus.</div></div>
  <div class="abs ico bg-blue" style="left:120px;top:48px;width:14px;height:14px">◎</div>
  <div class="abs" style="left:20px;top:130px;width:95px;text-align:right"><div class="h6 c-green">Goal Refresh</div><div class="tiny">Nullam eu tempor elit, et mattis lectus vel risus.</div></div>
  <div class="abs ico bg-green" style="left:120px;top:132px;width:14px;height:14px">✦</div>
  <div class="abs ico bg-grey" style="left:262px;top:45px;width:14px;height:14px">◆</div>
  <div class="abs" style="left:282px;top:42px;width:95px"><div class="h6 c-grey">Well Designed</div><div class="tiny">Nullam eu tempor elit, et mattis lectus vel risus.</div></div>
  <div class="abs ico bg-orange" style="left:262px;top:130px;width:14px;height:14px">✉</div>
  <div class="abs" style="left:282px;top:128px;width:95px"><div class="h6 c-orange">Notifications</div><div class="tiny">Nullam eu tempor elit, et mattis lectus vel risus.</div></div>
  <div class="foot"><b>TARN RIDGE</b><span>© Copyright 2024 Tarn Ridge Partners</span><span>14</span></div>
</section>

<section class="slide">
  <div class="photo ph-soft" style="inset:0 0 40px 0" role="img" aria-label="Faded photo of a city skyline"></div>
  <svg class="abs" style="left:20px;top:30px" width="360" height="151" viewBox="0 0 360 151">
    <rect x="22" y="90" width="18" height="61" fill="#1a6fb5"/><rect x="42" y="62" width="18" height="89" fill="#e8702a"/>
    <rect x="112" y="100" width="18" height="51" fill="#1a6fb5"/><rect x="132" y="40" width="18" height="111" fill="#e8702a"/>
    <rect x="202" y="103" width="18" height="48" fill="#1a6fb5"/><rect x="222" y="116" width="18" height="35" fill="#e8702a"/>
    <rect x="292" y="118" width="18" height="33" fill="#1a6fb5"/><rect x="312" y="134" width="18" height="17" fill="#e8702a"/>
    <g font-family="Lato" font-size="5" fill="#666" text-anchor="middle"><text x="31" y="86">400</text><text x="51" y="58">520</text><text x="121" y="96">350</text><text x="141" y="36">600</text><text x="211" y="99">280</text><text x="231" y="112">210</text><text x="301" y="114">200</text><text x="321" y="130">100</text></g>
  </svg>
  <div class="abs bg-grey" style="left:0;right:0;bottom:0;height:40px;display:flex;color:#fff;text-align:center">
    <div style="flex:1;padding-top:5px"><div class="h6">Asia</div><div class="tiny" style="color:#eee">Lorem ipsum dolor sit amet</div></div>
    <div style="flex:1;padding-top:5px"><div class="h6">Africa</div><div class="tiny" style="color:#eee">Lorem ipsum dolor sit amet</div></div>
    <div style="flex:1;padding-top:5px"><div class="h6">America</div><div class="tiny" style="color:#eee">Lorem ipsum dolor sit amet</div></div>
    <div style="flex:1;padding-top:5px"><div class="h6">Euro</div><div class="tiny" style="color:#eee">Lorem ipsum dolor sit amet</div></div>
  </div>
</section>

<section class="slide">
  <div class="ttl">Trending In The World</div>
  <div class="photo" style="left:20px;top:40px;width:240px;height:130px;background:linear-gradient(180deg,#ececec,#dcdcdc)" role="img" aria-label="World map in light grey"></div>
  <div class="abs" style="left:34px;top:90px;width:26px;height:26px;border-radius:50%;background:#8ab3d8;color:#fff;font-size:6px;display:flex;align-items:center;justify-content:center">25%</div>
  <div class="abs" style="left:104px;top:64px;width:34px;height:34px;border-radius:50%;background:#a6a6a6;color:#fff;font-size:8px;display:flex;align-items:center;justify-content:center">80%</div>
  <div class="abs" style="left:208px;top:70px;width:30px;height:30px;border-radius:50%;background:#8ccd5a;color:#fff;font-size:7px;display:flex;align-items:center;justify-content:center">75%</div>
  <div class="abs" style="left:178px;top:118px;width:20px;height:20px;border-radius:50%;background:#f08a48;color:#fff;font-size:5px;display:flex;align-items:center;justify-content:center">11%</div>
  <div class="abs" style="left:280px;top:45px"><span class="ico bg-blue">●</span></div><div class="abs" style="left:296px;top:44px;width:80px"><div class="h6 c-blue">Consulting</div><div class="tiny">Nullam tempor elit et mattis.</div></div>
  <div class="abs" style="left:280px;top:82px"><span class="ico bg-grey">●</span></div><div class="abs" style="left:296px;top:81px;width:80px"><div class="h6 c-grey">Strengths</div><div class="tiny">Nullam tempor elit et mattis.</div></div>
  <div class="abs" style="left:280px;top:119px"><span class="ico bg-orange">●</span></div><div class="abs" style="left:296px;top:118px;width:80px"><div class="h6 c-orange">Performance</div><div class="tiny">Nullam tempor elit et mattis.</div></div>
  <div class="foot"><b>TARN RIDGE</b><span>© Copyright 2024 Tarn Ridge Partners</span><span>16</span></div>
</section>

<section class="slide">
  <div class="ttl">Usa Map</div>
  <div class="photo" style="left:20px;top:40px;width:190px;height:120px;background:linear-gradient(135deg,#c6cbd1,#8f98a2)" role="img" aria-label="Map of the United States with highlighted branch states"></div>
  <div class="abs h6" style="left:225px;top:58px;color:#333">BRANCHES ANALYSIS</div>
  <div class="abs" style="left:225px;top:70px;font-size:18px;font-weight:700;color:var(--blue)">89%</div>
  <div class="abs tiny" style="left:262px;top:72px;width:115px">Of regions with an active deal pipeline this year.</div>
  <div class="abs tiny" style="left:225px;top:96px;width:150px">Lorem ipsum dolor sit amet, consectetur adipiscing elit sed do eiusmod tempor.</div>
  <div class="abs" style="left:225px;top:116px;width:150px"><table class="data"><tr><th>Branches</th><th>2021</th><th>2022</th><th>2023</th><th>2024</th></tr><tr><td>Branch count</td><td>21</td><td>27</td><td>32</td><td>40</td></tr></table></div>
  <div class="foot"><b>TARN RIDGE</b><span>© Copyright 2024 Tarn Ridge Partners</span><span>17</span></div>
</section>

<section class="slide">
  <div class="ttl">Three Column Description</div>
  <div class="abs c-blue" style="left:10px;top:30px;width:260px;font-size:6.5px">This is a place for your header text, insert your text here, just replace this text with your own text</div>
  <div class="abs small" style="left:10px;top:52px;width:115px">Lorem ipsum dolor sit amet, consectetur adipiscing elit, sed do eiusmod tempor incididunt ut labore et dolore magna aliqua. Ut enim ad minim veniam.<br><br>Duis aute irure dolor in reprehenderit in voluptate velit esse cillum dolore eu fugiat.</div>
  <div class="abs small" style="left:138px;top:52px;width:115px">Lorem ipsum dolor sit amet, consectetur adipiscing elit, sed do eiusmod tempor incididunt ut labore et dolore magna aliqua. Ut enim ad minim veniam.<br><br>Duis aute irure dolor in reprehenderit in voluptate velit esse cillum dolore eu fugiat.</div>
  <div class="abs small" style="left:266px;top:44px;width:115px">Lorem ipsum dolor sit amet, consectetur adipiscing elit, sed do eiusmod tempor incididunt ut labore et dolore magna aliqua. Ut enim ad minim veniam.<br><br>Duis aute irure dolor in reprehenderit in voluptate velit esse cillum dolore eu fugiat.</div>
  <div class="foot"><b>TARN RIDGE</b><span>© Copyright 2024 Tarn Ridge Partners</span><span>18</span></div>
</section>

<section class="slide">
  <div class="ttl">Our Team</div>
  <div class="photo" style="left:155px;top:36px;width:86px;height:86px;border-radius:50%;background:linear-gradient(160deg,#c9d2db,#7d8894)" role="img" aria-label="Portrait of team member"></div>
  <div class="abs" style="left:100px;top:128px;width:196px;text-align:center"><div class="h6" style="color:#333">Mr. Alan Forde</div><div class="tiny" style="color:var(--blue)">CEO</div><div class="tiny">Lorem ipsum dolor sit amet consectetur adipiscing elit sed do eiusmod tempor.</div></div>
  <div class="abs" style="left:180px;top:162px;display:flex;gap:3px"><span class="dot bg-blue"></span><span class="dot bg-blue"></span><span class="dot bg-blue"></span><span class="dot bg-blue"></span><span class="dot bg-blue"></span></div>
  <div class="foot"><b>TARN RIDGE</b><span>© Copyright 2024 Tarn Ridge Partners</span><span>19</span></div>
</section>

<section class="slide">
  <div class="ttl">Monthly Subscription</div>
  <div class="abs bg-blue" style="left:0;right:0;top:112px;height:99px"></div>
  <div class="abs" style="left:72px;top:55px;width:75px;height:108px;background:#fff;box-shadow:0 0 3px rgba(0,0,0,.2)"><div class="bg-green wt" style="height:26px;text-align:center;font-size:12px;padding-top:3px">$300<div style="font-size:3.5px">per month</div></div><div class="tiny" style="text-align:center;line-height:2.6">Single Edition<br>Unlimited Access<br>1 User<br>Free Update</div></div>
  <div class="abs" style="left:160px;top:40px;width:75px;height:124px;background:#fff;box-shadow:0 0 3px rgba(0,0,0,.2)"><div class="bg-grey wt" style="height:30px;text-align:center;font-size:14px;padding-top:4px">$900<div style="font-size:3.5px">per month</div></div><div class="tiny" style="text-align:center;line-height:3">Business Edition<br>Unlimited Access<br>5 User<br>Free Update</div></div>
  <div class="abs" style="left:248px;top:55px;width:75px;height:108px;background:#fff;box-shadow:0 0 3px rgba(0,0,0,.2)"><div class="bg-orange wt" style="height:26px;text-align:center;font-size:12px;padding-top:3px">$400<div style="font-size:3.5px">per month</div></div><div class="tiny" style="text-align:center;line-height:2.6">Single Edition<br>Unlimited Access<br>3 User<br>Free Update</div></div>
</section>

<section class="slide">
  <div class="ttl">Your Title Goes Here</div>
  <div class="abs tiny" style="left:10px;top:30px;width:340px"><b style="color:var(--blue)">Description:</b> Lorem ipsum dolor sit amet, consectetur adipiscing elit sed do eiusmod tempor incididunt ut labore et dolore magna.</div>
  <div class="abs" style="left:10px;top:46px;width:374px">
    <table class="data">
      <tr><th></th><th>Year</th><th>Year</th><th>Year</th><th>Year</th></tr>
      <tr><td>Lorem ipsum</td><td>50</td><td>35</td><td>12</td><td>36</td></tr>
      <tr><td>Lorem ipsum</td><td>33</td><td>22</td><td>43</td><td>23</td></tr>
      <tr><td>Lorem ipsum</td><td>65</td><td>34</td><td>32</td><td>34</td></tr>
      <tr><td>Lorem ipsum</td><td>45</td><td>56</td><td>41</td><td>12</td></tr>
      <tr><td>Lorem ipsum</td><td>23</td><td>17</td><td>21</td><td>52</td></tr>
      <tr><td>Lorem ipsum</td><td>76</td><td>45</td><td>34</td><td>53</td></tr>
      <tr><td>Lorem ipsum</td><td>33</td><td>62</td><td>23</td><td>32</td></tr>
      <tr><td>Lorem ipsum</td><td>44</td><td>12</td><td>28</td><td>17</td></tr>
      <tr><td>Lorem ipsum</td><td>58</td><td>24</td><td>50</td><td>22</td></tr>
      <tr><td>Lorem ipsum</td><td>51</td><td>44</td><td>36</td><td>10</td></tr>
      <tr><td>Lorem ipsum</td><td>70</td><td>35</td><td>29</td><td>41</td></tr>
    </table>
  </div>
  <div class="foot"><b>TARN RIDGE</b><span>© Copyright 2024 Tarn Ridge Partners</span><span>21</span></div>
</section>

<section class="slide">
  <div class="ttl">Our Team</div>
  <div class="photo" style="left:20px;top:38px;width:36px;height:36px;border-radius:50%;background:linear-gradient(160deg,#c9d2db,#7d8894)" role="img" aria-label="Portrait of team member"></div>
  <div class="abs" style="left:62px;top:36px;width:120px"><div class="h6" style="color:#333">Owen Marsh</div><div class="tiny" style="color:var(--blue)">CEO</div><div class="tiny">Lorem ipsum dolor sit amet elit.<br>• Sed do eiusmod tempor<br>• Ut labore et dolore magna</div></div>
  <div class="photo" style="left:210px;top:38px;width:36px;height:36px;border-radius:50%;background:linear-gradient(160deg,#c9d2db,#7d8894)" role="img" aria-label="Portrait of team member"></div>
  <div class="abs" style="left:252px;top:36px;width:120px"><div class="h6" style="color:#333">Leo Brandt</div><div class="tiny" style="color:var(--blue)">MBA</div><div class="tiny">Lorem ipsum dolor sit amet elit.<br>• Sed do eiusmod tempor<br>• Ut labore et dolore magna</div></div>
  <div class="photo" style="left:20px;top:110px;width:36px;height:36px;border-radius:50%;background:linear-gradient(160deg,#c9d2db,#7d8894)" role="img" aria-label="Portrait of team member"></div>
  <div class="abs" style="left:62px;top:108px;width:120px"><div class="h6" style="color:#333">Nina Hale</div><div class="tiny" style="color:var(--blue)">MBA</div><div class="tiny">Lorem ipsum dolor sit amet elit.<br>• Sed do eiusmod tempor<br>• Ut labore et dolore magna</div></div>
  <div class="photo" style="left:210px;top:110px;width:36px;height:36px;border-radius:50%;background:linear-gradient(160deg,#c9d2db,#7d8894)" role="img" aria-label="Portrait of team member"></div>
  <div class="abs" style="left:252px;top:108px;width:120px"><div class="h6" style="color:#333">Paul Ivers</div><div class="tiny" style="color:var(--blue)">Partner</div><div class="tiny">Lorem ipsum dolor sit amet elit.<br>• Sed do eiusmod tempor<br>• Ut labore et dolore magna</div></div>
  <div class="foot"><b>TARN RIDGE</b><span>© Copyright 2024 Tarn Ridge Partners</span><span>22</span></div>
</section>

<section class="slide">
  <div class="ttl">Sales Comparison</div>
  <svg class="abs" style="left:0;top:30px" width="394" height="150" viewBox="0 0 394 150">
    <g font-family="Lato" font-size="5" text-anchor="middle" fill="#666">
      <text x="75" y="8">2016 Sales</text><text x="315" y="8">2016 Sales</text>
      <line x1="20" y1="110" x2="140" y2="110" stroke="#ccc" stroke-width=".6"/>
      <rect x="28" y="50" width="12" height="60" fill="#1a6fb5"/><rect x="56" y="38" width="12" height="72" fill="#1a6fb5"/><rect x="84" y="44" width="12" height="66" fill="#1a6fb5"/><rect x="112" y="30" width="12" height="80" fill="#1a6fb5"/>
      <text x="34" y="46">320</text><text x="62" y="34">390</text><text x="90" y="40">350</text><text x="118" y="26">420</text>
      <line x1="254" y1="110" x2="374" y2="110" stroke="#ccc" stroke-width=".6"/>
      <rect x="262" y="54" width="12" height="56" fill="#e8702a"/><rect x="290" y="42" width="12" height="68" fill="#e8702a"/><rect x="318" y="36" width="12" height="74" fill="#e8702a"/><rect x="346" y="26" width="12" height="84" fill="#e8702a"/>
      <text x="268" y="50">300</text><text x="296" y="38">370</text><text x="324" y="32">400</text><text x="352" y="22">460</text>
    </g>
    <line x1="197" y1="15" x2="197" y2="135" stroke="#bbb" stroke-dasharray="2 2" stroke-width=".8"/>
    <circle cx="197" cy="75" r="10" fill="#9b9b9b"/><text x="197" y="78" font-size="7" text-anchor="middle" fill="#fff" font-family="Lato">VS</text>
  </svg>
  <div class="abs" style="left:22px;top:165px;font-size:17px;font-weight:700;color:var(--blue)">45%</div>
  <div class="abs tiny" style="left:62px;top:167px;width:80px"><span class="h6" style="color:var(--blue)">Lorem ipsum dolor</span><br>Sed do eiusmod tempor.</div>
  <div class="abs" style="left:256px;top:165px;font-size:17px;font-weight:700;color:var(--orange)">68%</div>
  <div class="abs tiny" style="left:296px;top:167px;width:80px"><span class="h6" style="color:var(--orange)">Lorem ipsum dolor</span><br>Sed do eiusmod tempor.</div>
  <div class="foot"><b>TARN RIDGE</b><span>© Copyright 2024 Tarn Ridge Partners</span><span>23</span></div>
</section>

<section class="slide">
  <div class="ttl">Bullet &amp; Chart Area</div>
  <svg class="abs" style="left:70px;top:32px" width="150" height="150" viewBox="0 0 42 42">
    <circle cx="21" cy="21" r="8" fill="none" stroke="#1a6fb5" stroke-width="16" stroke-dasharray="30.2 50.3" transform="rotate(-90 21 21)"/>
    <circle cx="21" cy="21" r="8" fill="none" stroke="#9b9b9b" stroke-width="16" stroke-dasharray="0 30.2 12.6 50.3" transform="rotate(-90 21 21)"/>
    <circle cx="21" cy="21" r="8" fill="none" stroke="#e8702a" stroke-width="16" stroke-dasharray="0 42.8 7.5 50.3" transform="rotate(-90 21 21)"/>
    <circle cx="21" cy="21" r="8" fill="none" stroke="#7ab648" stroke-width="16" stroke-dasharray="0 50.3 5 50.3" transform="rotate(-90 21 21)"/>
  </svg>
  <div class="abs" style="left:228px;top:100px;font-size:11px;color:#777">60%</div>
  <div class="abs" style="left:50px;top:132px;font-size:11px;color:#777">25%</div>
  <div class="abs" style="left:44px;top:88px;font-size:11px;color:var(--orange)">15%</div>
  <div class="abs" style="left:88px;top:38px;font-size:11px;color:var(--green)">10%</div>
  <div class="abs" style="left:262px;top:40px"><span class="ico bg-blue">⌕</span></div><div class="abs" style="left:278px;top:39px;width:100px"><div class="h6 c-blue">Category One</div><div class="tiny">Lorem ipsum dolor sit amet elit.</div></div>
  <div class="abs" style="left:262px;top:72px"><span class="ico bg-grey">✎</span></div><div class="abs" style="left:278px;top:71px;width:100px"><div class="h6 c-grey">Category Two</div><div class="tiny">Lorem ipsum dolor sit amet elit.</div></div>
  <div class="abs" style="left:262px;top:104px"><span class="ico bg-orange">⌕</span></div><div class="abs" style="left:278px;top:103px;width:100px"><div class="h6 c-orange">Category Three</div><div class="tiny">Lorem ipsum dolor sit amet elit.</div></div>
  <div class="abs" style="left:262px;top:136px"><span class="ico bg-green">✦</span></div><div class="abs" style="left:278px;top:135px;width:100px"><div class="h6 c-green">Category Four</div><div class="tiny">Lorem ipsum dolor sit amet elit.</div></div>
  <div class="foot"><b>TARN RIDGE</b><span>© Copyright 2024 Tarn Ridge Partners</span><span>24</span></div>
</section>

<section class="slide">
  <div class="ttl">Bullet &amp; Chart Area</div>
  <svg class="abs" style="left:10px;top:40px" width="220" height="140" viewBox="0 0 220 140">
    <g font-family="Lato" font-size="4.5" fill="#777">
      <text x="0" y="20">Category 1</text><text x="0" y="50">Category 2</text><text x="0" y="80">Category 3</text><text x="0" y="110">Category 4</text>
    </g>
    <line x1="28" y1="4" x2="28" y2="122" stroke="#ccc" stroke-width=".6"/>
    <rect x="28" y="12" width="120" height="5" fill="#1a6fb5"/><rect x="28" y="18" width="70" height="5" fill="#e8702a"/><rect x="28" y="24" width="90" height="5" fill="#9b9b9b"/>
    <rect x="28" y="42" width="95" height="5" fill="#1a6fb5"/><rect x="28" y="48" width="150" height="5" fill="#e8702a"/><rect x="28" y="54" width="60" height="5" fill="#9b9b9b"/>
    <rect x="28" y="72" width="110" height="5" fill="#1a6fb5"/><rect x="28" y="78" width="55" height="5" fill="#e8702a"/><rect x="28" y="84" width="140" height="5" fill="#9b9b9b"/>
    <rect x="28" y="102" width="170" height="5" fill="#1a6fb5"/><rect x="28" y="108" width="100" height="5" fill="#e8702a"/><rect x="28" y="114" width="75" height="5" fill="#9b9b9b"/>
    <g font-family="Lato" font-size="4" fill="#777"><rect x="60" y="130" width="4" height="4" fill="#1a6fb5"/><text x="66" y="134">Series 1</text><rect x="95" y="130" width="4" height="4" fill="#e8702a"/><text x="101" y="134">Series 2</text><rect x="130" y="130" width="4" height="4" fill="#9b9b9b"/><text x="136" y="134">Series 3</text></g>
  </svg>
  <div class="abs" style="left:250px;top:40px"><span class="ico bg-blue">⌕</span></div><div class="abs" style="left:266px;top:39px;width:110px"><div class="h6 c-blue">Category One</div><div class="tiny">Lorem ipsum dolor sit amet elit.</div></div>
  <div class="abs" style="left:250px;top:72px"><span class="ico bg-grey">✎</span></div><div class="abs" style="left:266px;top:71px;width:110px"><div class="h6 c-grey">Category Two</div><div class="tiny">Lorem ipsum dolor sit amet elit.</div></div>
  <div class="abs" style="left:250px;top:104px"><span class="ico bg-orange">⌕</span></div><div class="abs" style="left:266px;top:103px;width:110px"><div class="h6 c-orange">Category Three</div><div class="tiny">Lorem ipsum dolor sit amet elit.</div></div>
  <div class="abs" style="left:250px;top:136px"><span class="ico bg-green">✦</span></div><div class="abs" style="left:266px;top:135px;width:110px"><div class="h6 c-green">Category Four</div><div class="tiny">Lorem ipsum dolor sit amet elit.</div></div>
  <div class="foot"><b>TARN RIDGE</b><span>© Copyright 2024 Tarn Ridge Partners</span><span>25</span></div>
</section>

<section class="slide">
  <div class="ttl">Column Chart</div>
  <svg class="abs" style="left:10px;top:30px" width="374" height="110" viewBox="0 0 374 110">
    <line x1="0" y1="108" x2="374" y2="108" stroke="#ccc" stroke-width=".6"/>
    <g font-family="Lato" font-size="6" text-anchor="middle">
      <rect x="14" y="18" width="18" height="90" fill="#1a6fb5"/><rect x="36" y="53" width="18" height="55" fill="#9b9b9b"/><rect x="58" y="71" width="18" height="37" fill="#e8702a"/>
      <text x="23" y="14" fill="#1a6fb5">49</text><text x="45" y="49" fill="#9b9b9b">30</text><text x="67" y="67" fill="#e8702a">20</text>
      <rect x="106" y="62" width="18" height="46" fill="#1a6fb5"/><rect x="128" y="27" width="18" height="81" fill="#9b9b9b"/><rect x="150" y="68" width="18" height="40" fill="#e8702a"/>
      <text x="115" y="58" fill="#1a6fb5">25</text><text x="137" y="23" fill="#9b9b9b">44</text><text x="159" y="64" fill="#e8702a">22</text>
      <rect x="198" y="42" width="18" height="66" fill="#1a6fb5"/><rect x="220" y="84" width="18" height="24" fill="#9b9b9b"/><rect x="242" y="25" width="18" height="83" fill="#e8702a"/>
      <text x="207" y="38" fill="#1a6fb5">36</text><text x="229" y="80" fill="#9b9b9b">13</text><text x="251" y="21" fill="#e8702a">45</text>
      <rect x="290" y="9" width="18" height="99" fill="#1a6fb5"/><rect x="312" y="47" width="18" height="61" fill="#9b9b9b"/><rect x="334" y="47" width="18" height="61" fill="#e8702a"/>
      <text x="299" y="7" fill="#1a6fb5">54</text><text x="321" y="43" fill="#9b9b9b">33</text><text x="343" y="43" fill="#e8702a">33</text>
    </g>
  </svg>
  <div class="abs" style="left:18px;top:146px;width:80px;text-align:center"><div class="h6 c-blue">Category 1</div><div class="tiny">Lorem ipsum dolor sit amet elit sed do.</div></div>
  <div class="abs" style="left:110px;top:146px;width:80px;text-align:center"><div class="h6 c-blue">Category 2</div><div class="tiny">Lorem ipsum dolor sit amet elit sed do.</div></div>
  <div class="abs" style="left:202px;top:146px;width:80px;text-align:center"><div class="h6 c-blue">Category 3</div><div class="tiny">Lorem ipsum dolor sit amet elit sed do.</div></div>
  <div class="abs" style="left:294px;top:146px;width:80px;text-align:center"><div class="h6 c-blue">Category 4</div><div class="tiny">Lorem ipsum dolor sit amet elit sed do.</div></div>
  <div class="foot"><b>TARN RIDGE</b><span>© Copyright 2024 Tarn Ridge Partners</span><span>26</span></div>
</section>

<section class="slide">
  <div class="ttl">Basic Chevron Process</div>
  <svg class="abs" style="left:10px;top:90px" width="374" height="22" viewBox="0 0 374 22">
    <polygon points="0,4 70,4 78,11 70,18 0,18 6,11" fill="#2a8ad0"/>
    <polygon points="74,4 146,4 154,11 146,18 74,18 82,11" fill="#9b9b9b"/>
    <polygon points="150,4 222,4 230,11 222,18 150,18 158,11" fill="#e8702a"/>
    <polygon points="226,4 298,4 306,11 298,18 226,18 234,11" fill="#7ab648"/>
    <polygon points="302,4 372,4 374,11 372,18 302,18 310,11" fill="#0d2a4a"/>
  </svg>
  <div class="abs ico" style="left:38px;top:94px;width:14px;height:14px;background:#1a6fb5;border:1.5px solid #fff">✈</div>
  <div class="abs ico" style="left:114px;top:70px;width:14px;height:14px;background:#2a8ad0">✎</div>
  <div class="abs ico" style="left:190px;top:116px;width:14px;height:14px;background:#9b9b9b">⌕</div>
  <div class="abs ico" style="left:266px;top:70px;width:14px;height:14px;background:#e8702a">★</div>
  <div class="abs ico" style="left:342px;top:116px;width:14px;height:14px;background:#0d2a4a">▭</div>
  <div class="abs" style="left:84px;top:34px;width:74px;text-align:center"><div class="h6" style="color:#333">Idea</div><div class="tiny">Lorem ipsum dolor sit amet elit sed do eiusmod.</div></div>
  <div class="abs" style="left:236px;top:34px;width:74px;text-align:center"><div class="h6" style="color:#333">Brainstorming</div><div class="tiny">Lorem ipsum dolor sit amet elit sed do eiusmod.</div></div>
  <div class="abs" style="left:8px;top:132px;width:74px;text-align:center"><div class="h6" style="color:#333">Research</div><div class="tiny">Lorem ipsum dolor sit amet elit sed do eiusmod.</div></div>
  <div class="abs" style="left:160px;top:134px;width:74px;text-align:center"><div class="h6" style="color:#333">Search</div><div class="tiny">Lorem ipsum dolor sit amet elit sed do eiusmod.</div></div>
  <div class="abs" style="left:312px;top:134px;width:74px;text-align:center"><div class="h6" style="color:#333">Strategy</div><div class="tiny">Lorem ipsum dolor sit amet elit sed do eiusmod.</div></div>
  <div class="foot"><b>TARN RIDGE</b><span>© Copyright 2024 Tarn Ridge Partners</span><span>27</span></div>
</section>

<section class="slide" style="background:var(--grey)">
  <div class="abs bg-blue" style="left:0;right:0;top:82px;height:22px"></div>
  <div class="abs" style="left:42px;top:78px;width:100px;height:30px;background:#5b9fd6"></div>
  <div class="abs brand" style="left:58px;top:84px;font-size:9px">TARN RIDGE<br>PARTNERS</div>
  <div class="abs wt" style="left:54px;top:150px;font-size:16px;font-weight:300">THIS IS YOUR DIVIDER PAGE</div>
  <div class="abs wt" style="left:54px;top:172px;font-size:5.5px">Your Subtitle Goes Here</div>
</section>

<section class="slide">
  <div class="ttl">Three Steps</div>
  <div class="abs" style="left:20px;top:40px"><span class="ico bg-blue">↗</span></div><div class="abs" style="left:36px;top:39px;width:180px"><div class="h6 c-blue">Sample Text</div><div class="tiny">Lorem ipsum dolor sit amet, consectetur adipiscing elit sed do eiusmod tempor.</div></div>
  <div class="abs" style="left:20px;top:90px"><span class="ico bg-grey">↻</span></div><div class="abs" style="left:36px;top:89px;width:180px"><div class="h6 c-grey">Sample Text</div><div class="tiny">Lorem ipsum dolor sit amet, consectetur adipiscing elit sed do eiusmod tempor.</div></div>
  <div class="abs" style="left:20px;top:140px"><span class="ico bg-orange">⌕</span></div><div class="abs" style="left:36px;top:139px;width:180px"><div class="h6 c-orange">Sample Text</div><div class="tiny">Lorem ipsum dolor sit amet, consectetur adipiscing elit sed do eiusmod tempor.</div></div>
  <svg class="abs" style="left:228px;top:22px" width="160" height="180" viewBox="0 0 160 180">
    <circle cx="100" cy="45" r="28" fill="none" stroke="#1a6fb5" stroke-width="18"/>
    <circle cx="50" cy="88" r="28" fill="none" stroke="#9b9b9b" stroke-width="18" stroke-dasharray="120 56" transform="rotate(40 50 88)"/>
    <circle cx="100" cy="131" r="28" fill="none" stroke="#e8702a" stroke-width="18"/>
    <text x="100" y="49" font-size="12" text-anchor="middle" fill="#1a6fb5">↗</text><text x="100" y="135" font-size="12" text-anchor="middle" fill="#e8702a">⌕</text>
  </svg>
  <div class="foot"><b>TARN RIDGE</b><span>© Copyright 2024 Tarn Ridge Partners</span><span>29</span></div>
</section>

<section class="slide">
  <div class="photo ph-blue" style="inset:0" role="img" aria-label="Blue-toned photo of a glass skyscraper"></div>
  <div class="abs brand" style="left:28px;top:100px;font-size:11px">TARN RIDGE<br>PARTNERS</div>
  <div class="abs" style="left:136px;top:100px;width:1px;height:24px;background:#fff"></div>
  <div class="abs wt" style="left:150px;top:100px;font-size:19px;font-weight:300">THANK YOU...</div>
  <div class="abs wt" style="right:14px;bottom:10px;font-size:5px">www.tarnridgepartners.com</div>
</section>

</main>
</body>
</html>
```